Flyer Design Project - Brightwell Fitness

I am looking for a flyer to distribute to multiple locations and target markets. It is for an Brightwell Fitness.
Special Promo (Biggest thing to highlight)
"Summer is FREE"
Need to have "When you Join Now"
Smaller details: Some Restrictions Apply
Need Brightwell Fitness Logo
24-Hour Access
Some photo to highlight a workout preferably a female as we tend to be a little more female than male.
Please see the attached files for the logo and a sample mailer we have done in the past. Color scheme of purple is needed.
Can examples be made to fit on a 5.47" Wide Flyer by 4.21" Tall.
Single Sided Flyer
Industry/Entity Type
Fitness
Look and feel
Each slider illustrates characteristics of the customer's brand and the style your logo design should communicate.

```html
<!DOCTYPE html>
<html lang="en">
<head>
<meta charset="utf-8">
<title>Brightwell Fitness – Summer is Free Flyer</title>
<link rel="stylesheet" href="https://fonts.googleapis.com/css2?family=Bebas+Neue&family=Oswald:wght@500;600&display=swap">
<style>
  :root {
    --purple: #8a6fc4;
    --purple-deep: #6f54ad;
    --pink: #ec1f8e;
    --ink: #2a2a2e;
    --white: #ffffff;
    --panel: rgba(190, 225, 222, 0.72);
    --page: #ffffff;
  }
  * { margin: 0; padding: 0; box-sizing: border-box; }
  html, body {
    width: 1200px;
    height: 1000px;
    overflow: hidden;
    background: var(--page);
  }
  .canvas {
    position: relative;
    width: 1200px;
    height: 1000px;
  }
  .flyer {
    position: absolute;
    left: 50px;
    top: 77px;
    width: 1100px;
    height: 846px;
    overflow: hidden;
    background: var(--ink);
  }
  .band-top {
    position: absolute;
    left: 0; top: 0;
    width: 100%;
    height: 16px;
    background: var(--purple);
    z-index: 3;
  }
  .band-bottom {
    position: absolute;
    left: 0; bottom: 0;
    width: 100%;
    height: 38px;
    background: var(--purple);
    z-index: 3;
  }
  .workout-photo {
    position: absolute;
    left: 0; top: 16px;
    width: 100%;
    height: 792px;
    background:
      radial-gradient(ellipse 30% 38% at 28% 50%, rgba(226, 58, 140, 0.55), transparent 70%),
      radial-gradient(ellipse 26% 20% at 42% 76%, rgba(40, 170, 180, 0.45), transparent 70%),
      linear-gradient(180deg, #e4e6e6 0%, #cfd3d4 38%, #8a8c92 68%, #1f1f24 100%);
  }
  .promo-panel {
    position: absolute;
    left: 54%;
    top: 16px;
    width: 39.5%;
    height: 730px;
    background: var(--panel);
    text-align: center;
    z-index: 2;
  }
  .promo-line {
    font-family: "Bebas Neue", sans-serif;
    color: var(--purple-deep);
    font-size: 104px;
    line-height: 0.9;
    letter-spacing: 4px;
  }
  .promo-line.first { margin-top: 34px; }
  .promo-free {
    font-family: "Bebas Neue", sans-serif;
    color: var(--pink);
    font-size: 200px;
    line-height: 0.85;
    letter-spacing: 6px;
    margin-top: 4px;
  }
  .promo-join {
    font-family: "Oswald", sans-serif;
    font-weight: 600;
    color: var(--ink);
    font-size: 38px;
    line-height: 1;
    margin-top: 4px;
  }
  .promo-fine {
    font-family: "Oswald", sans-serif;
    font-weight: 500;
    color: var(--ink);
    font-size: 12px;
    letter-spacing: 1px;
    margin-top: 6px;
  }
  .palm-scene {
    position: absolute;
    left: 0;
    bottom: 70px;
    width: 100%;
    height: 150px;
    background: linear-gradient(180deg, rgba(60, 95, 80, 0) 0%, rgba(60, 95, 80, 0.35) 50%, rgba(200, 150, 90, 0.35) 100%);
  }
  .access {
    position: absolute;
    left: 8%;
    top: 700px;
    font-family: "Bebas Neue", sans-serif;
    font-size: 84px;
    letter-spacing: 5px;
    color: var(--white);
    line-height: 1;
    z-index: 4;
  }
  .brand-box {
    position: absolute;
    left: 65%;
    top: 702px;
    width: 210px;
    height: 64px;
    background: var(--white);
    display: flex;
    align-items: center;
    justify-content: center;
    gap: 10px;
    z-index: 4;
  }
  .brand-mark {
    width: 16px;
    height: 16px;
    background: var(--purple-deep);
  }
  .brand-name {
    font-family: "Oswald", sans-serif;
    font-weight: 600;
    font-size: 21px;
    color: var(--purple-deep);
    text-transform: uppercase;
    letter-spacing: 0.5px;
  }
</style>
</head>
<body>
<div class="canvas">
  <section class="flyer">
    <div class="band-top"></div>
    <div class="workout-photo" role="img" aria-label="Smiling woman in a pink top riding a spin bike in a bright gym class, other riders behind her"></div>

    <div class="promo-panel">
      <p class="promo-line first">Summer</p>
      <p class="promo-line">Is</p>
      <p class="promo-free">Free</p>
      <p class="promo-join">WHEN YOU JOIN NOW</p>
      <p class="promo-fine">SOME RESTRICTIONS APPLY</p>
      <div class="palm-scene" role="img" aria-label="Faint silhouette of palm trees on a sunset beach"></div>
    </div>

    <p class="access">24 Hour Access</p>

    <div class="brand-box">
      <span class="brand-mark"></span>
      <span class="brand-name">Brightwell Fitness</span>
    </div>

    <div class="band-bottom"></div>
  </section>
</div>
</body>
</html>
```